依頼詳細
記載項目の内容を含んだ、 85.6mm × 54.0mmのICカード(一般的なカードと同じサイズ)に印刷可能なデザインをお願い致します。
カードは横向きなので、縦向きのデザインは不可と致します。

(1)弊社のロゴ(※添付ファイル)に合うもの
(2)「ハイテクさ(技術力)」「クリーンさ(清潔感)」
が感じられるデザインを求めております。

※ロゴの配色は、添付ファイルのもの(グラデーション)からデザインに合わせて変更し単色等にして頂いても問題ありません

・トンボ(トリムマーク)をつけて下さい。
・フチなしのデザインなどは必ず仕上がり線より外側に3mm程度の塗り足しを入れて下さい。
・顔写真または半身写真など:仮として、グレーに塗りつぶした人物のシルエットでデザインに入れ込んでください。
記載項目
●表面内容
①名前欄
②社員番号欄
③発行日欄
④顔写真欄
⑤会社名:KVT株式会社
⑥本社住所
〒241-0815
神奈川県相模原市南区北見坂3丁目8番21号
TEL 042-618-3940(代表) FAX 042-619-2856
⑦「上記のものは当社の従業員であることを証明する」の一文

●裏面内容
・弊社の経営理念
「時代と共に進化を続け、最適な快適環境を提供する」

・注意事項
本証は当社社員であることを証明するものである
このカードを他人に貸与又は譲渡しないこと
本証は常時携帯すること
本証を紛失、破損した場合は直ちに届け出ること
退職時は直ちに返納すること
本証を取得された方は当社にご連絡ください
希望イメージ
シンプル 複雑
単色 カラフル
暗い 明るい
日常 高級
遊び心 厳粛
未来的 伝統的
女性的 男性的
希望する色
青系、緑系、グレー系
納品ファイル
• 高解像度JPG (.jpg)
• イラストレーター形式 (.ai)
• フォトショップ形式 (.psd)
• PNG形式 (.png)
補足説明
他社の知的財産権・商標を侵すようなデザイン等の提案は決してしないようにお願い致します。
著作権の盗用や侵害するデザイン案は厳禁になります。
素材テンプレートの流用やアレンジも不可です。
皆様からのご提案、誠にありがとうございます。
よりイメージの付きやすいデザインが可能となるよう、希望内容を追記させていただく事となりました。
ご一読の程、よろしくお願い致します。

●追加希望内容
カラーはグラデーション等の効果よりも、シンプルなものがベストです
依頼内容を明確にするため、さらに追加したい点がございましたので、期間延長の上追記させて頂きます。ご確認の程よろしくお願い致します。

●写真のサイズは免許証と同じ程度の大きさでお願い致します
●写真素材を使用したものよりも、デザインのみのシンプルなものがベストです

表面・裏面共にシンプルかつスマートなデザインで、弊社内でも最も多数から好評でありましたので当選とさせて頂きました。

今回のコンペにご参加頂きました皆様、素晴らしいデザイン案を多数頂きまして誠にありがとうございます。

次回募集を行う事がございましたら、改めましてご参加頂ければ幸いです。

```html
<!DOCTYPE html>
<html lang="ja">
<head>
<meta charset="utf-8">
<title>KVT株式会社 社員証</title>
<link rel="stylesheet" href="https://fonts.googleapis.com/css2?family=Noto+Sans+JP:wght@400;500;700&family=Noto+Serif+JP:wght@500;700&display=swap">
<style>
  :root {
    --brand-blue: #2f88cc;
    --brand-blue-deep: #1f6fb0;
    --panel-blue: #5aa3d8;
    --ink: #333333;
    --ink-soft: #555555;
    --rule: #bfc6cc;
    --photo-gray: #8d8f92;
    --photo-bg: #d9dadc;
    --paper: #ffffff;
    --page: #ffffff;
  }
  * { box-sizing: border-box; margin: 0; padding: 0; }
  html, body {
    width: 887px; height: 1200px; overflow: hidden;
    background: var(--page);
    font-family: "Noto Sans JP", sans-serif;
    color: var(--ink);
  }
  .card {
    position: absolute;
    left: 89px;
    width: 716px;
    box-shadow: 0 0 0 1px #e2e5e8;
    overflow: hidden;
  }
  /* ---------- front ---------- */
  .card--front { top: 34px; height: 557px; background: var(--paper); }
  .id-photo {
    position: absolute; left: 30px; top: 75px; width: 178px; height: 227px;
    background: linear-gradient(180deg, var(--photo-bg) 0%, var(--photo-gray) 100%);
  }
  .company {
    position: absolute; left: 340px; top: 108px;
    display: flex; align-items: center; gap: 10px;
    font-weight: 700; font-size: 36px; color: var(--brand-blue-deep);
    letter-spacing: 1px;
  }
  .company__dot { width: 30px; height: 30px; border-radius: 50%; background: var(--brand-blue); }
  .holder-name {
    position: absolute; left: 355px; top: 222px;
    font-size: 54px; font-weight: 500; letter-spacing: 30px; color: var(--ink);
  }
  .issue-row {
    position: absolute; right: 26px; top: 318px;
    font-size: 19px; color: var(--ink-soft); display: flex; gap: 40px;
  }
  .divider {
    position: absolute; left: 30px; right: 26px; top: 350px;
    height: 2px; background: var(--rule);
  }
  .address {
    position: absolute; left: 30px; top: 362px; width: 640px;
    font-size: 19px; line-height: 23px; color: var(--ink);
  }
  .address .tel { padding-left: 70px; }
  .certify-band {
    position: absolute; left: 0; right: 0; top: 440px; height: 50px;
    background: var(--brand-blue);
    color: #fff; font-size: 20px; letter-spacing: 1px;
    display: flex; align-items: center; justify-content: center;
  }
  /* ---------- back ---------- */
  .card--back { top: 623px; height: 548px; background: var(--brand-blue); color: #fff; }
  .philosophy { text-align: center; }
  .philosophy__label { margin-top: 62px; font-size: 21px; letter-spacing: 2px; }
  .philosophy__text {
    margin-top: 8px;
    font-family: "Noto Serif JP", serif; font-weight: 700;
    font-size: 45px; line-height: 58px; letter-spacing: 3px;
  }
  .notices {
    position: absolute; left: 74px; top: 238px; width: 577px; height: 235px;
    background: var(--panel-blue);
    border: 1px solid rgba(255,255,255,0.45);
    list-style: none; padding: 20px 26px;
    font-size: 17px; line-height: 32px;
  }
  .notices li::before { content: "・"; }
</style>
</head>
<body>
  <section class="card card--front" aria-label="社員証 表面">
    <div class="id-photo" role="img" aria-label="顔写真欄(グレーの人物シルエット)"></div>
    <div class="company"><span class="company__dot"></span>KVT株式会社</div>
    <div class="holder-name">社員名前</div>
    <div class="issue-row"><span>社員番号 012345</span><span>2019年7月1日発行</span></div>
    <div class="divider"></div>
    <div class="address">
      <p>〒241-0815 神奈川県相模原市南区北見坂3丁目8番21号</p>
      <p class="tel">TEL 042-618-3940(代表) FAX 042-619-2856</p>
    </div>
    <div class="certify-band">上記のものは当社の従業員であることを証明する</div>
  </section>

  <section class="card card--back" aria-label="社員証 裏面">
    <div class="philosophy">
      <p class="philosophy__label">〈経営理念〉</p>
      <p class="philosophy__text">時代と共に進化を続け<br>最適な快適環境を提供する</p>
    </div>
    <ul class="notices">
      <li>本証は当社社員であることを証明するものである</li>
      <li>このカードを他人に貸与又は譲渡しないこと</li>
      <li>本証は常時携帯すること</li>
      <li>本証を紛失、破損した場合は直ちに届け出ること</li>
      <li>退職時は直ちに返納すること</li>
      <li>本証を取得された方は当社にご連絡ください</li>
    </ul>
  </section>
</body>
</html>
```